Baby Making Project

We need a poster design for a surrogacy/ivf clinic. We would like the poster to be used as office artwork and to say something like

'We came here as a couple, we left as a family'

The poster should have some family related picture in it, but not necessarily the standard mother, father and child image.
The services are used by many single and gay parents so we don't want to alienate anyone.
The poster should like modern, perhaps with the use of animals photo, or animated looking characters so you can't make out whether the parents are male/female.

```html
<!DOCTYPE html>
<html lang="en">
<head>
<meta charset="utf-8">
<title>We came here as a couple, we left as a family</title>
<link rel="stylesheet" href="https://fonts.googleapis.com/css2?family=Dancing+Script:wght@400;500&display=swap">
<style>
  :root {
    --sky-top: #cde6f7;
    --sky-mid: #b4daf2;
    --sky-low: #9fcdea;
    --fur-light: #f6eed8;
    --fur-warm: #eadbb5;
    --snow: #ffffff;
    --letter-fill: #ffffff;
    --letter-outline: #14285a;
  }
  * { margin: 0; padding: 0; box-sizing: border-box; }
  html, body {
    width: 849px;
    height: 1200px;
    overflow: hidden;
    background: var(--snow);
  }
  .poster {
    position: relative;
    width: 849px;
    height: 1200px;
    overflow: hidden;
  }
  .poster__photo {
    position: absolute;
    inset: 0;
    background:
      radial-gradient(ellipse 70% 22% at 52% 86%, var(--fur-light) 0%, var(--fur-warm) 55%, rgba(234,219,181,0) 100%),
      linear-gradient(180deg, var(--sky-top) 0%, var(--sky-mid) 45%, var(--sky-low) 75%, var(--snow) 92%, var(--snow) 100%);
  }
  .poster__quote {
    position: absolute;
    inset: 0;
    font-family: "Dancing Script", cursive;
    font-weight: 400;
    color: var(--letter-fill);
    -webkit-text-stroke: 2px var(--letter-outline);
    paint-order: stroke fill;
  }
  .quote__line {
    position: absolute;
    left: 0;
    width: 849px;
    text-align: center;
    white-space: nowrap;
    line-height: 1;
  }
  .quote__line--one   { top: 0;    font-size: 150px; }
  .quote__line--two   { top: 175px; font-size: 155px; }
  .quote__line--three { top: 365px; font-size: 200px; }
  .quote__line--four  { top: 560px; font-size: 255px; }
  .quote__small { font-size: 160px; margin-right: 30px; }
</style>
</head>
<body>
  <main class="poster">
    <div class="poster__photo" role="img" aria-label="Photograph of a family of polar bears sleeping curled together on snow under a pale blue arctic sky"></div>
    <h1 class="poster__quote">
      <span class="quote__line quote__line--one">We came here</span>
      <span class="quote__line quote__line--two">as a couple,</span>
      <span class="quote__line quote__line--three">we left as</span>
      <span class="quote__line quote__line--four"><span class="quote__small">a</span>family</span>
    </h1>
  </main>
</body>
</html>
```